Talvora Companies Business Card Design

We need a new business card for our Private Equity Real Estate Development firm, “Talvora” and our EB-5 regional center “Mossgate Regional Center” on one card. We prefer a design that is simple, elegant, and represents the luxury products we design and build as well as the financial security and stability our successful history has produced. We are an industry leader in our field and 3rd generation family business that has evolved into an institutional quality investment platform. Considered design size is standard business card dimensions (3.5 x 2 inches with an additional 1/8 inch space for design elements or backgrounds that extend beyond the finished size of your piece.

Target Market(s)

• High net worth individuals
• Highly skilled technical workers and physicians in the US seeking investment-based immigration opportunities
• Sophisticated private equity investors
• Intermediary partners include domestic attorneys and investment brokers, as well as international agent networks
• US real estate developers

Industry/Entity Type

Finance

Contact Information for Business Card

(Providing placeholder info for personal information, please design for longer character spaces, longer names and addresses etc..)
• Logo for Talvora
• Logo for Mossgate Regional Center
• Full name: Dermot Talvora
• Job title: CEO
• Email address: dtalvora@talvoracompanies.com
• Cell phone number: +1.555.314.2786
• Office number +1.555.862.4071
• Office address: Quillfield Park 7, 4817 Vista Loma, San Ramon, CA.
• Website: www.talvoracompanies.com

Font styles to use
Serif
Sans Serif

Colors
ec1f27
ffffff
000000

Requirements
Must have
• • Logo for Talvora
• • Logo for Mossgate Regional Center
• - Use rounded corners
• (See .ai file included for logos)
Nice to have
• • Simple, elegant design
• • Aesthetically compatible with our website design (www.talvoracompanies.com)
• • Color palette including but not limited to white, black, and red (as per logos)
Should not have
• - Not too much red color
• - Do not stack both logos on top of each other

```html
<!DOCTYPE html>
<html lang="en">
<head>
<meta charset="utf-8">
<title>Talvora Companies – Business Card</title>
<link href="https://fonts.googleapis.com/css2?family=Cinzel:wght@600;700&family=Lato:wght@400;700&display=swap" rel="stylesheet">
<style>
  :root {
    --stage: #2c2d30;
    --stage-light: #45464a;
    --card-dark: #4a4b4e;
    --card-light: #ffffff;
    --crimson: #a3182f;
    --ink: #3a3b3e;
    --ink-soft: #555659;
    --rule: #9a9a9c;
  }
  * { margin: 0; padding: 0; box-sizing: border-box; }
  html, body { width: 1200px; height: 900px; overflow: hidden; }
  body {
    position: relative;
    background: radial-gradient(circle at 60% 35%, var(--stage-light), var(--stage) 70%);
    font-family: "Lato", sans-serif;
  }
  .card {
    position: absolute;
    width: 620px;
    height: 354px;
    border-radius: 28px;
    overflow: hidden;
    box-shadow: 0 18px 40px rgba(0,0,0,.45);
  }
  /* Back side */
  .card-back {
    left: 80px; top: 70px;
    background: var(--card-dark);
    display: flex; align-items: center; justify-content: center; gap: 14px;
  }
  .brand-mark { width: 22px; height: 22px; background: var(--crimson); flex: none; }
  .back-brand {
    font-family: "Cinzel", serif; font-weight: 700;
    font-size: 28px; letter-spacing: 1px;
    color: var(--crimson);
  }
  /* Front side */
  .card-front {
    left: 500px; top: 470px;
    background: var(--card-light);
  }
  .front-brand {
    position: absolute; left: 44px; top: 72px;
    display: flex; align-items: center; gap: 16px;
  }
  .front-brand .brand-mark { background: var(--ink); width: 26px; height: 26px; }
  .front-brand .brand-name {
    font-family: "Cinzel", serif; font-weight: 700;
    font-size: 34px; letter-spacing: 1px; color: var(--ink);
  }
  .person {
    position: absolute; left: 150px; top: 160px;
    padding-left: 12px; border-left: 2px solid var(--crimson);
  }
  .person-name {
    font-family: "Cinzel", serif; font-weight: 700;
    font-size: 23px; color: var(--crimson); line-height: 1.15;
  }
  .person-title { font-size: 14px; color: var(--ink-soft); }
  .contact-list {
    position: absolute; left: 172px; top: 232px;
    list-style: none;
    padding-left: 14px; border-left: 1px solid var(--rule);
  }
  .contact-list li {
    display: flex; align-items: center; gap: 10px;
    font-size: 15px; color: var(--ink); line-height: 22px;
  }
  .contact-list svg { width: 14px; height: 14px; fill: var(--crimson); flex: none; }
  .address {
    position: absolute; right: 36px; top: 132px;
    font-style: normal;
    text-align: right; font-size: 14px; line-height: 19px; color: var(--ink);
  }
  .edge-band {
    position: absolute; left: 0; right: 0; bottom: 0; height: 10px;
    display: flex;
  }
  .edge-band .band-red { flex: 3; background: var(--crimson); }
  .edge-band .band-grey { flex: 1; background: var(--card-dark); }
</style>
</head>
<body>

<section class="card card-back" aria-label="Card back">
  <span class="brand-mark"></span>
  <span class="back-brand">Mossgate Regional Center</span>
</section>

<section class="card card-front" aria-label="Card front">
  <div class="front-brand">
    <span class="brand-mark"></span>
    <span class="brand-name">Talvora Capital</span>
  </div>

  <div class="person">
    <p class="person-name">Dermot Talvora</p>
    <p class="person-title">CEO</p>
  </div>

  <ul class="contact-list">
    <li>
      <svg viewBox="0 0 16 16"><path d="M4 0h8a1 1 0 0 1 1 1v14a1 1 0 0 1-1 1H4a1 1 0 0 1-1-1V1a1 1 0 0 1 1-1zm1 2v10h6V2zm3 11a1 1 0 1 0 0 2 1 1 0 0 0 0-2z"/></svg>
      +1.555.314.2786
    </li>
    <li>
      <svg viewBox="0 0 16 16"><path d="M3.6 1l2.5 3-1.4 1.8a9 9 0 0 0 5.5 5.5L12 9.9l3 2.5-1.6 2.5C7.3 15 1 8.7 1.1 2.6z"/></svg>
      +1.555.862.4071
    </li>
    <li>
      <svg viewBox="0 0 16 16"><path d="M1 3h14v10H1zm1.5 1.2v.5L8 8.5l5.5-3.8v-.5z"/></svg>
      dtalvora@talvoracompanies.com
    </li>
    <li>
      <svg viewBox="0 0 16 16"><path d="M8 0a8 8 0 1 0 0 16A8 8 0 0 0 8 0zm0 1.5c.9 0 2 1.9 2.3 5.5H5.7C6 3.4 7.1 1.5 8 1.5zM1.6 7h2.6c.1-2 .5-3.8 1.2-4.9A6.5 6.5 0 0 0 1.6 7zm0 2a6.5 6.5 0 0 0 3.8 4.9C4.7 12.8 4.3 11 4.2 9zm4.1 0h4.6c-.3 3.6-1.4 5.5-2.3 5.5S6 12.6 5.7 9zm6.1 0h2.6a6.5 6.5 0 0 1-3.8 4.9c.7-1.1 1.1-2.9 1.2-4.9zm2.6-2h-2.6c-.1-2-.5-3.8-1.2-4.9A6.5 6.5 0 0 1 14.4 7z"/></svg>
      www.talvoracompanies.com
    </li>
  </ul>

  <address class="address">
    4817 Vista Loma<br>
    Suite 410, Larkmoor<br>
    California 94516.
  </address>

  <div class="edge-band"><span class="band-red"></span><span class="band-grey"></span></div>
</section>

</body>
</html>
```